A Website for our Indian Wedding

We need a webdesign for our website. The site will have several pages, but we should only need two different designs: one for the front page and one for the internal content pages. Attached are some assets, a sample of some kolams that we have have access to and could be incorporated into the design as well as the save the date email, which we could be used as inspiration.

Please feel free to use stock content or photos which we can replace with our own.

Target Market(s)

Guests of our wedding

Industry/Entity Type

Wedding

Coding

Coded - Design and coding required

Number of Pages Required

2 page

Font styles to use
Serif

Requirements
Must have
• A bold front page, an internal page design for the content. Similar colors to the save the date email.
Nice to have
• it would be nice if the design were done in a well-known HTML/CSS framework like Zurb Foundation.

```html
<!DOCTYPE html>
<html lang="en">
<head>
<meta charset="utf-8">
<title>Mira &amp; Jonah — Wedding</title>
<link href="https://fonts.googleapis.com/css2?family=Great+Vibes&family=Lora:ital,wght@0,400;0,700;1,400&family=Open+Sans:wght@400;600&display=swap" rel="stylesheet">
<style>
  :root{
    --bg-dark:#2a0507;
    --bg-deep:#4a0a0e;
    --red:#b8141b;
    --red-soft:#c41e24;
    --gold:#f2c46a;
    --gold-light:#ffe3a1;
    --gold-dark:#b9822c;
    --cream:#fbe9c9;
    --text-soft:#f3cfc0;
    --line:rgba(242,196,106,.55);
  }
  *{box-sizing:border-box;margin:0;padding:0}
  html,body{width:1200px;height:2332px;overflow:hidden}
  body{position:relative;background:radial-gradient(ellipse at center,var(--bg-deep),var(--bg-dark) 75%);font-family:"Lora",Georgia,serif;color:var(--cream)}
  .frame{position:absolute;left:0;top:0}
  .abs{position:absolute}
  .center{left:0;width:1200px;text-align:center}

  .couple-title{top:100px;font-family:"Great Vibes",cursive;font-size:104px;color:var(--gold);font-weight:400;line-height:1}
  .portrait{width:300px;height:300px;border-radius:50%;background:radial-gradient(circle,#d59a3c 0,#9c6120 60%,#6d3a10 100%);border:6px solid var(--gold-dark);top:240px;display:flex;align-items:center;justify-content:center}
  .portrait span{width:210px;height:210px;border-radius:50%;background:radial-gradient(circle at 50% 40%,#b9634a,#5a2218 80%);border:4px solid var(--gold)}
  .portrait.left{left:250px}
  .portrait.right{left:650px}

  .main-nav{top:632px;left:112px;width:976px;height:72px;background:linear-gradient(#ffe39a,#e6b04b 55%,#c98d2c);border-top:2px solid var(--gold-light);border-bottom:2px solid var(--gold-dark);display:flex;align-items:center;justify-content:space-between;padding:0 28px}
  .main-nav a{font-family:"Lora",serif;font-size:17px;letter-spacing:1.5px;color:#6a1a08;text-decoration:none;text-transform:uppercase}
  .main-nav .arrow{width:0;height:0;border-top:9px solid transparent;border-bottom:9px solid transparent}
  .main-nav .arrow.l{border-right:12px solid #8a2a0c}
  .main-nav .arrow.r{border-left:12px solid #8a2a0c}

  .section-title{font-family:"Great Vibes",cursive;font-size:64px;color:var(--gold);font-weight:400;line-height:1}
  .section-title::after{content:"";display:block;width:220px;height:2px;margin:10px auto 0;background:linear-gradient(90deg,transparent,var(--gold),transparent)}

  .event-card{top:848px;height:240px;border:1px solid var(--line);text-align:center;padding:22px 30px}
  .event-card .icon{width:58px;height:58px;margin:0 auto 14px;display:block}
  .event-card h3{font-family:"Lora",serif;font-weight:400;font-size:20px;letter-spacing:1px;color:var(--cream);text-transform:uppercase;margin-bottom:12px}
  .event-card p{font-size:14px;line-height:1.6;color:var(--text-soft)}
  .read-more{display:inline-block;margin-top:12px;font-size:13px;color:var(--gold);text-decoration:none}

  .gallery{top:1252px;left:100px;width:1000px;height:176px;display:flex;gap:4px}
  .gallery .photo{flex:1;height:176px}
  .gallery-captions{top:1450px;left:100px;width:1000px;display:flex}
  .gallery-captions span{flex:1;text-align:center;font-style:italic;font-size:20px;color:var(--cream)}

  .intro{top:1610px;left:230px;width:740px;text-align:center;font-size:14px;line-height:1.7;font-style:italic;color:var(--text-soft)}

  .stay-card{top:1680px;height:200px;border:1px solid var(--line);padding:22px 24px;display:flex;align-items:center;gap:22px}
  .stay-card.left{left:120px;width:480px}
  .stay-card.right{left:610px;width:480px}
  .stay-card .thumb{flex:none;width:130px;height:130px;border-radius:50%;border:4px solid var(--gold)}
  .stay-card h4{font-family:"Lora",serif;font-weight:400;font-style:italic;font-size:17px;color:var(--cream);margin-bottom:8px}
  .stay-card p{font-size:13px;line-height:1.6;color:var(--text-soft)}
  .stay-card .date{margin-top:8px;font-size:12px;font-style:italic;color:var(--gold)}

  .info-title{top:1930px;font-family:"Open Sans",sans-serif;font-size:34px;color:var(--cream)}
  .info-text{top:1984px;left:240px;width:720px;text-align:center;font-size:13px;line-height:1.8;color:var(--text-soft)}
  .info-date{top:2070px;font-family:"Open Sans",sans-serif;font-size:30px;color:var(--gold)}
  .copyright{top:2296px;right:24px;font-family:"Open Sans",sans-serif;font-size:12px;color:var(--text-soft)}
</style>
</head>
<body>

<svg class="frame" width="1200" height="2332" viewBox="0 0 1200 2332" aria-hidden="true">
  <defs>
    <radialGradient id="paper" cx="50%" cy="40%" r="70%">
      <stop offset="0" stop-color="#c81c22"/>
      <stop offset="1" stop-color="#a5121a"/>
    </radialGradient>
  </defs>
  <path fill="url(#paper)" d="
    M 300 0 L 900 0
    Q 960 60 1040 40 Q 1100 90 1080 170
    Q 1150 240 1110 330 Q 1150 420 1110 520
    L 1110 1800
    Q 1150 1880 1110 1960 Q 1160 2040 1100 2120
    Q 1120 2210 1030 2240 Q 960 2300 860 2270
    Q 760 2332 600 2300 Q 440 2332 340 2270
    Q 240 2300 170 2240 Q 80 2210 100 2120
    Q 40 2040 90 1960 Q 50 1880 90 1800
    L 90 520
    Q 50 420 90 330 Q 50 240 120 170
    Q 100 90 160 40 Q 240 60 300 0 Z"/>
  <path fill="none" stroke="rgba(242,196,106,.35)" stroke-width="2" d="
    M 320 24 L 880 24 Q 940 80 1016 64 Q 1066 104 1054 176
    Q 1116 244 1084 330 Q 1116 420 1084 520 L 1084 1800
    Q 1116 1880 1084 1960 Q 1126 2040 1076 2112
    Q 1090 2190 1016 2216 Q 950 2270 860 2244
    Q 760 2300 600 2272 Q 440 2300 340 2244
    Q 250 2270 184 2216 Q 110 2190 124 2112
    Q 74 2040 116 1960 Q 84 1880 116 1800 L 116 520
    Q 84 420 116 330 Q 84 244 146 176 Q 134 104 184 64 Q 260 80 320 24 Z"/>
</svg>

<header>
  <h1 class="abs center couple-title">Mira &amp; Jonah</h1>
  <div class="abs portrait left" role="img" aria-label="Portrait of the bride in a gold ornamental frame"><span></span></div>
  <div class="abs portrait right" role="img" aria-label="Portrait of the groom in a gold ornamental frame"><span></span></div>
</header>

<nav class="abs main-nav">
  <span class="arrow l"></span>
  <a href="#">Home</a>
  <a href="#">Our Story</a>
  <a href="#">Gallery</a>
  <a href="#">Accommodation</a>
  <a href="#">Events</a>
  <a href="#">Contact Us</a>
  <span class="arrow r"></span>
</nav>

<h2 class="abs center section-title" style="top:760px">Events &amp; Parties</h2>

<article class="abs event-card" style="left:104px;width:300px">
  <svg class="icon" viewBox="0 0 58 58"><circle cx="29" cy="29" r="27" fill="none" stroke="#f2c46a" stroke-width="2"/><path d="M24 19 L36 16 L36 36" fill="none" stroke="#fbe9c9" stroke-width="2.5"/><circle cx="21" cy="39" r="4" fill="#fbe9c9"/><circle cx="33" cy="37" r="4" fill="#fbe9c9"/><path d="M24 19 L24 39" stroke="#fbe9c9" stroke-width="2.5"/></svg>
  <h3>Bachelor Party</h3>
  <p>Join us for an evening of music, dancing and laughter with friends and family before the big day.</p>
  <a class="read-more" href="#">Read More ›</a>
</article>

<article class="abs event-card" style="left:440px;width:320px">
  <svg class="icon" viewBox="0 0 58 58"><circle cx="29" cy="29" r="27" fill="none" stroke="#f2c46a" stroke-width="2"/><path d="M29 42 C22 33 20 29 20 25 A9 9 0 0 1 38 25 C38 29 36 33 29 42 Z" fill="#fbe9c9"/><circle cx="29" cy="25" r="3.5" fill="#b8141b"/></svg>
  <h3>Wedding Location</h3>
  <p>The ceremony will be held in the temple gardens, followed by dinner and celebrations under the stars.</p>
  <a class="read-more" href="#">Read More ›</a>
</article>

<article class="abs event-card" style="left:792px;width:304px">
  <svg class="icon" viewBox="0 0 58 58"><circle cx="29" cy="29" r="27" fill="none" stroke="#f2c46a" stroke-width="2"/><rect x="18" y="26" width="22" height="15" fill="#fbe9c9"/><rect x="16" y="21" width="26" height="6" fill="#fbe9c9"/><rect x="27.5" y="21" width="3" height="20" fill="#b8141b"/><path d="M29 21 C25 14 19 17 24 21 M29 21 C33 14 39 17 34 21" fill="none" stroke="#fbe9c9" stroke-width="2"/></svg>
  <h3>Gift Registry</h3>
  <p>Your presence is our greatest gift, but for those who wish, a small registry is available online.</p>
  <a class="read-more" href="#">Read More ›</a>
</article>

<h2 class="abs center section-title" style="top:1150px">Photo Gallery</h2>

<section class="abs gallery">
  <div class="photo" role="img" aria-label="Photo of the engagement ceremony" style="background:linear-gradient(135deg,#8a2a1c,#d0843a)"></div>
  <div class="photo" role="img" aria-label="Photo of the mehendi function" style="background:linear-gradient(135deg,#c9483a,#e9a15a)"></div>
  <div class="photo" role="img" aria-label="Photo of the muhurtham" style="background:linear-gradient(135deg,#d88f7a,#f0c3a6)"></div>
  <div class="photo" role="img" aria-label="Photo of the reception" style="background:linear-gradient(135deg,#6e1a22,#c25a4a)"></div>
</section>
<div class="abs gallery-captions">
  <span>Our Engagement</span><span>Mehendi Function</span><span>Our Muhurtham</span><span>Our Reception</span>
</div>

<h2 class="abs center section-title" style="top:1520px">Accomodation</h2>
<p class="abs intro">We have reserved rooms at two nearby hotels for our guests. Please book early to secure the group rate and mention our names.</p>

<article class="abs stay-card left">
  <div>
    <h4>The Garden Palace Hotel</h4>
    <p>A short walk from the venue with spacious rooms, a rooftop restaurant and free breakfast.</p>
    <p class="date">▪ January 13, 2016 (Check-in)</p>
  </div>
  <div class="thumb" role="img" aria-label="Photo of the hotel" style="background:linear-gradient(#7fb7d8 45%,#c99a3a 45%,#8a5a1e)"></div>
</article>

<article class="abs stay-card right">
  <div class="thumb" role="img" aria-label="Photo of the inn" style="background:linear-gradient(#8fc2e0 40%,#e0b862 40%,#a86a2a)"></div>
  <div>
    <h4>Riverside Heritage Inn</h4>
    <p>A quiet retreat by the water with shuttle service to all wedding events each day.</p>
    <p class="date">▪ January 14, 2016 (Check-in)</p>
  </div>
</article>

<h2 class="abs center info-title" style="font-weight:400">Important Information</h2>
<p class="abs info-text">Please arrive thirty minutes before each ceremony. Traditional attire is welcome, and parking is available on site for all guests. Kindly confirm your attendance by the first of December.</p>
<p class="abs center info-date">January 13 &amp; 14, 2016</p>

<footer class="abs copyright">© Copyright 2015 MiraJonah All Rights reserved.</footer>

</body>
</html>
```